Business Card Design

Harbourline Recruitment is a specialist financial services recruitment company and implementation partner

Industry/Entity Type

Business

Contact Information for Business Card

Tom Ashford
Harbourline Recruitment Ltd
e:tom.ashford@harbourline-staffing.com
m:07834 206 148
m:07712 438 560
s: tommashford

```html
<!DOCTYPE html>
<html lang="en">
<head>
<meta charset="utf-8">
<title>Harbourline Recruitment – Business Card</title>
<link rel="stylesheet" href="https://fonts.googleapis.com/css2?family=Open+Sans:wght@400;600;800&display=swap">
<style>
  :root {
    --page: #3a332f;
    --card: #1b1b1b;
    --card-edge: #111111;
    --green: #6cc02a;
    --white: #f2f2f2;
    --muted: #e6e6e6;
  }
  * { box-sizing: border-box; margin: 0; padding: 0; }
  html, body {
    width: 1200px; height: 844px; overflow: hidden;
    background: var(--page);
    font-family: "Open Sans", Arial, sans-serif;
  }
  .stage {
    position: relative; width: 1200px; height: 844px;
  }
  .card {
    position: absolute; top: 263px;
    width: 540px; height: 318px;
    background: var(--card);
    border: 1px solid var(--card-edge);
    box-shadow: 0 10px 24px rgba(0,0,0,.45);
    overflow: hidden;
  }
  .card--front { left: 40px; }
  .card--back { left: 620px; }

  .brand {
    position: absolute; display: flex; align-items: center; gap: 16px;
  }
  .brand__mark {
    width: 78px; height: 78px; border-radius: 50%;
    border: 3px solid var(--white); flex: none;
  }
  .brand__name {
    color: var(--green); font-weight: 800; font-size: 21px;
    line-height: 1.1; letter-spacing: 1px; text-transform: uppercase;
    width: 250px;
  }
  .card--front .brand { left: 34px; top: 68px; }
  .card--back .brand { left: 118px; top: 118px; }

  .divider {
    position: absolute; left: 0; right: 0; top: 170px;
    height: 1px; background: var(--green); opacity: .8;
  }

  .holder {
    position: absolute; right: 22px; top: 140px;
    color: var(--green); font-size: 17px; font-weight: 400;
  }
  .contacts {
    position: absolute; right: 22px; top: 180px;
    list-style: none; text-align: right;
  }
  .contacts li {
    display: flex; justify-content: flex-end; align-items: center; gap: 10px;
    color: var(--muted); font-size: 13.5px; height: 22px;
  }
  .contacts svg { width: 11px; height: 11px; flex: none; }
  .email {
    position: absolute; right: 22px; top: 276px;
    color: var(--muted); font-size: 14px;
  }
</style>
</head>
<body>
<main class="stage">
  <section class="card card--front" aria-label="Business card front">
    <div class="brand">
      <span class="brand__mark"></span>
      <span class="brand__name">Harbourline Recruitment Ltd</span>
    </div>
    <div class="divider"></div>
    <p class="holder">Tom Ashford</p>
    <ul class="contacts">
      <li>07834 206 148
        <svg viewBox="0 0 11 11"><rect x="2.5" y="0.5" width="6" height="10" rx="1" fill="none" stroke="var(--green)"/></svg></li>
      <li>07712 438 560
        <svg viewBox="0 0 11 11"><rect x="2.5" y="0.5" width="6" height="10" rx="1" fill="none" stroke="var(--green)"/></svg></li>
      <li>harbourline-staffing.com
        <svg viewBox="0 0 11 11"><rect x="0.5" y="2" width="10" height="7" fill="var(--green)"/><path d="M0.5 2 L5.5 6 L10.5 2" fill="none" stroke="var(--card)"/></svg></li>
      <li>tommashford
        <svg viewBox="0 0 11 11"><circle cx="5.5" cy="5.5" r="5.5" fill="var(--green)"/></svg></li>
    </ul>
    <p class="email">tom.ashford@harbourline-staffing.com</p>
  </section>

  <section class="card card--back" aria-label="Business card back">
    <div class="brand">
      <span class="brand__mark"></span>
      <span class="brand__name">Harbourline Recruitment Ltd</span>
    </div>
  </section>
</main>
</body>
</html>
```